BrivoLane Ute.

I want the full logo on one side. And the other side the card if right Ralf the logo the left half orange like the car in the logo color with Danielle R Morrow
Founder and CEO
Email symbol then dmorrow@brivolaneute.com
Www symbol. Then Brivolaneute.com
Phone symbol then 413-926-BRIV
The very bottom would like Brivo Lane Ute is a division of Harmond Vistas. LLC

```html
<!DOCTYPE html>
<html lang="en">
<head>
<meta charset="UTF-8">
<title>Brivo Lane Ute – Business Cards</title>
<link href="https://fonts.googleapis.com/css2?family=Cormorant+SC:wght@600;700&family=Jost:wght@400;500&display=swap" rel="stylesheet">
<style>
  :root {
    --backdrop: #ebebeb;
    --card: #ffffff;
    --ink: #3b2a25;
    --muted: #4a4a4a;
    --orange: #f0932b;
    --orange-soft: #f7b566;
    --sand: #f6d9b3;
    --rule: #2f2f2f;
  }
  * { box-sizing: border-box; margin: 0; padding: 0; }
  html, body { width: 1200px; height: 900px; overflow: hidden; }
  body {
    background: var(--backdrop);
    position: relative;
    font-family: "Jost", "Helvetica Neue", Arial, sans-serif;
    color: var(--muted);
  }
  .card {
    position: absolute;
    width: 513px;
    height: 295px;
    background: var(--card);
    box-shadow: 0 3px 7px rgba(0,0,0,0.18);
    overflow: hidden;
  }
  .card--logo   { left: 73px;  top: 138px; }
  .card--white  { left: 616px; top: 138px; }
  .card--orange { left: 73px;  top: 465px; }
  .card--scene  { left: 616px; top: 465px; }

  /* logo lockup */
  .lockup { position: absolute; text-align: center; }
  .lockup__dot {
    display: block; margin: 0 auto;
    border-radius: 50%; background: var(--orange);
  }
  .lockup__name {
    font-family: "Cormorant SC", Georgia, serif;
    font-weight: 700; color: var(--ink);
    letter-spacing: 0.02em; white-space: nowrap; line-height: 1;
  }
  .lockup__tag {
    font-family: "Jost", Arial, sans-serif; font-weight: 500;
    color: var(--ink); letter-spacing: 0.12em; text-transform: uppercase;
    border-top: 1px solid var(--rule);
  }
  .card--logo .lockup { left: 0; right: 0; top: 84px; }
  .card--logo .lockup__dot { width: 74px; height: 74px; }
  .card--logo .lockup__name { font-size: 40px; margin-top: 10px; }
  .card--logo .lockup__tag { font-size: 9px; width: 266px; margin: 8px auto 0; padding-top: 6px; }

  .card--white .lockup, .card--orange .lockup { left: 40px; width: 196px; top: 84px; }
  .card--white .lockup__dot, .card--orange .lockup__dot { width: 44px; height: 44px; }
  .card--white .lockup__name, .card--orange .lockup__name { font-size: 25px; margin-top: 6px; }
  .card--white .lockup__tag, .card--orange .lockup__tag { font-size: 6.5px; padding-top: 4px; margin-top: 5px; }

  /* contact block */
  .contact { position: absolute; left: 288px; }
  .contact__name {
    font-family: "Cormorant SC", Georgia, serif; font-weight: 600;
    font-size: 19px; color: var(--ink); line-height: 1; text-transform: uppercase;
  }
  .contact__role {
    font-size: 10px; letter-spacing: 0.06em; text-transform: uppercase;
    color: var(--muted); margin-top: 4px;
  }
  .card--orange .contact__name,
  .card--orange .contact__role { color: var(--orange); font-family: "Jost", Arial, sans-serif; font-weight: 400; }
  .card--orange .contact__name { font-size: 17px; }
  .contact__list { list-style: none; margin-top: 14px; }
  .contact__item {
    display: flex; align-items: center; gap: 6px;
    font-size: 12.5px; color: var(--muted); height: 20px;
  }
  .contact__icon { width: 12px; height: 12px; flex: none; }
  .card--white .contact, .card--orange .contact { top: 96px; }
  .card--scene .contact { top: 122px; }
  .card--scene .contact__list { margin-top: 8px; }

  /* footer */
  .footer { position: absolute; left: 79px; width: 353px; top: 254px; text-align: center; }
  .footer__rule { height: 2px; background: var(--rule); margin: 0 10px; }
  .footer__text {
    font-size: 8.5px; letter-spacing: 0.07em; text-transform: uppercase;
    color: var(--ink); margin-top: 7px;
  }

  /* scene card */
  .scene-art {
    position: absolute; left: 0; top: 34px; width: 262px; height: 186px;
    background: linear-gradient(180deg, #ffffff 0%, #fbe7c8 22%, var(--orange-soft) 40%, var(--orange) 70%, var(--sand) 100%);
  }
  .scene-title {
    position: absolute; right: 40px; top: 44px;
    font-family: "Cormorant SC", Georgia, serif; font-weight: 700;
    font-size: 40px; color: var(--ink); line-height: 1; white-space: nowrap;
  }
</style>
</head>
<body>

<svg width="0" height="0" style="position:absolute" aria-hidden="true">
  <defs>
    <symbol id="icon-phone" viewBox="0 0 12 12">
      <circle cx="6" cy="6" r="5.5" fill="none" stroke="#f0932b" stroke-width="1"/>
      <path d="M4 3.4c.3-.2.6-.1.8.2l.5.8c.1.2.1.5-.1.6l-.4.3c.3.6.8 1.1 1.4 1.4l.3-.4c.2-.2.4-.2.6-.1l.8.5c.3.2.4.5.2.8-.4.7-1.1.9-1.8.6C5.2 7.6 4.4 6.8 3.9 5.8c-.3-.8-.4-1.7.1-2.4z" fill="#f0932b"/>
    </symbol>
    <symbol id="icon-mail" viewBox="0 0 12 12">
      <circle cx="6" cy="6" r="6" fill="#f0932b"/>
      <rect x="3" y="4" width="6" height="4.2" rx="0.5" fill="#fff"/>
      <path d="M3.2 4.3L6 6.4l2.8-2.1" fill="none" stroke="#f0932b" stroke-width="0.7"/>
    </symbol>
    <symbol id="icon-web" viewBox="0 0 12 12">
      <circle cx="6" cy="6" r="6" fill="#f0932b"/>
      <circle cx="6" cy="6" r="3.3" fill="none" stroke="#fff" stroke-width="0.7"/>
      <ellipse cx="6" cy="6" rx="1.4" ry="3.3" fill="none" stroke="#fff" stroke-width="0.7"/>
      <path d="M2.7 6h6.6" stroke="#fff" stroke-width="0.7"/>
    </symbol>
  </defs>
</svg>

<section class="card card--logo">
  <div class="lockup">
    <span class="lockup__dot"></span>
    <p class="lockup__name">BRIVO LANE UTE</p>
    <p class="lockup__tag">Ride the quiet shore</p>
  </div>
</section>

<section class="card card--white">
  <div class="lockup">
    <span class="lockup__dot"></span>
    <p class="lockup__name">BRIVO LANE UTE</p>
    <p class="lockup__tag">Ride the quiet shore</p>
  </div>
  <div class="contact">
    <p class="contact__name">Danielle R Morrow</p>
    <p class="contact__role">Founder and CEO</p>
    <ul class="contact__list">
      <li class="contact__item"><svg class="contact__icon"><use href="#icon-phone"/></svg>413 926 BRIV</li>
      <li class="contact__item"><svg class="contact__icon"><use href="#icon-mail"/></svg>dmorrow@brivolaneute.com</li>
      <li class="contact__item"><svg class="contact__icon"><use href="#icon-web"/></svg>Brivolaneute.com</li>
    </ul>
  </div>
  <div class="footer">
    <div class="footer__rule"></div>
    <p class="footer__text">Brivo Lane Ute is a division of Harmond Vistas LLC</p>
  </div>
</section>

<section class="card card--orange">
  <div class="lockup">
    <span class="lockup__dot"></span>
    <p class="lockup__name">BRIVO LANE UTE</p>
    <p class="lockup__tag">Ride the quiet shore</p>
  </div>
  <div class="contact">
    <p class="contact__name">Danielle R Morrow</p>
    <p class="contact__role">Founder and CEO</p>
    <ul class="contact__list">
      <li class="contact__item"><svg class="contact__icon"><use href="#icon-phone"/></svg>413 926 BRIV</li>
      <li class="contact__item"><svg class="contact__icon"><use href="#icon-mail"/></svg>dmorrow@brivolaneute.com</li>
      <li class="contact__item"><svg class="contact__icon"><use href="#icon-web"/></svg>Brivolaneute.com</li>
    </ul>
  </div>
  <div class="footer">
    <div class="footer__rule"></div>
    <p class="footer__text">Brivo Lane Ute is a division of Harmond Vistas LLC</p>
  </div>
</section>

<section class="card card--scene">
  <div class="scene-art" role="img" aria-label="Illustration of an orange vintage wagon with a surfboard on the roof and bottles in the window, beside a wooden beach fence under a rising sun"></div>
  <p class="scene-title">BRIVO LANE UTE</p>
  <div class="contact">
    <p class="contact__name">Danielle R Morrow</p>
    <p class="contact__role">Founder and CEO</p>
    <ul class="contact__list">
      <li class="contact__item"><svg class="contact__icon"><use href="#icon-phone"/></svg>413 926 BRIV</li>
      <li class="contact__item"><svg class="contact__icon"><use href="#icon-mail"/></svg>dmorrow@brivolaneute.com</li>
      <li class="contact__item"><svg class="contact__icon"><use href="#icon-web"/></svg>Brivolaneute.com</li>
    </ul>
  </div>
  <div class="footer">
    <div class="footer__rule"></div>
    <p class="footer__text">Brivo Lane Ute is a division of Harmond Vistas LLC</p>
  </div>
</section>

</body>
</html>
```